Boutique Store Selling Antiques and Unique Finds

I need a Web Page designed for my Store Called "Harrow Lane". I would like a very classic, muted design that looks European when pulled up. I will be selling Antiques from all over the world and Unique finds that have reproduced. I will also be selling high-end purses and jewelry with unique, reasonable products for the every-day buyer as well.

Target Market(s)

25-70 year old men and women;)

Coding

Number of Pages Required

1 page

Colors

Designer to choose only greyscale colors for use in the design.

Requirements
Must have
• I want it

```html
<!DOCTYPE html>
<html lang="en">
<head>
<meta charset="utf-8">
<title>Harrow Lane — Antiques &amp; Unique Finds</title>
<link href="https://fonts.googleapis.com/css2?family=Roboto:wght@300;400;500&family=Lora:ital,wght@0,400;0,500;0,700;1,400&family=Open+Sans:wght@400;600&display=swap" rel="stylesheet">
<style>
:root{
  --accent:#7d7d7d;
  --accent-light:#b4b4b4;
  --ink:#2f2f2f;
  --muted:#6f6f6f;
  --rule:#cfcfcf;
  --paper:#ffffff;
  --band:#ebebeb;
  --footer:#262626;
  --footer-text:#d9d9d9;
}
*{margin:0;padding:0;box-sizing:border-box}
html,body{width:1200px;height:3403px;overflow:hidden;background:var(--paper)}
body{position:relative;font-family:"Lora",serif;color:var(--ink)}
.abs{position:absolute}
.grid-line{position:absolute;top:622px;width:1px;height:2222px;background:#f3f3f3}
.brand{position:absolute;left:0;width:1200px;text-align:center;font-family:"Lora",serif;font-weight:500;letter-spacing:5px;text-transform:uppercase;color:var(--accent)}
.brand-dot{display:block;margin:0 auto 8px;width:14px;height:14px;border-radius:50%;background:var(--accent)}
.footer .brand{color:var(--accent-light)}
.footer .brand-dot{background:var(--accent-light)}
.nav{position:absolute;top:130px;left:0;width:1200px;font-family:"Lora",serif;font-size:11px;letter-spacing:.6px;text-transform:uppercase;color:#444}
.nav span{position:absolute;transform:translateX(-50%);white-space:nowrap}
.nav .active{color:var(--accent)}
.nav .active::after{content:"";position:absolute;left:-6px;right:-6px;top:22px;height:1px;background:var(--accent)}
.tools{position:absolute;top:48px}
.hero{position:absolute;left:12px;top:178px;width:1173px;height:444px;background:linear-gradient(100deg,#242424 0%,#3e3e3e 20%,#5a5a5a 35%,#333 50%,#666 70%,#2e2e2e 88%,#262626 100%)}
.hero-box{position:absolute;left:613px;top:336px;width:411px;height:179px;border:1px solid rgba(255,255,255,.55);background:rgba(20,20,20,.35);padding:34px 18px 0;color:#fff}
.hero-box h2{font-family:"Roboto",sans-serif;font-weight:400;font-size:29px;letter-spacing:.3px;line-height:1;white-space:nowrap}
.hero-box h2 em{font-style:normal;color:#cfcfcf}
.hero-box p{font-family:"Lora",serif;font-size:12px;line-height:21px;margin-top:12px;color:#eee}
.hero-box a{display:block;font-style:italic;font-size:11px;margin-top:12px;color:#fff}
.arrow{position:absolute}
.kicker{position:absolute;left:0;width:1200px;text-align:center;font-family:"Lora",serif;font-style:italic;font-size:17px;color:var(--accent)}
.title{position:absolute;left:0;width:1200px;text-align:center;font-family:"Roboto",sans-serif;font-weight:300;font-size:32px;letter-spacing:2px;color:#333}
.rule{position:absolute;height:1px;background:var(--rule)}
.card{position:absolute;top:843px;width:222px}
.card .photo{height:349px}
.card .label{position:absolute;left:0;top:283px;width:196px;height:66px;background:#fff;padding:20px 10px 0}
.card .label i{display:block;font-size:13px;color:var(--accent)}
.card .label b{display:block;font-family:"Roboto",sans-serif;font-weight:400;font-size:16px;letter-spacing:.5px;margin-top:6px;color:#333;text-transform:uppercase;white-space:nowrap}
.card p{font-family:"Roboto",sans-serif;font-weight:300;font-size:12.5px;line-height:24px;color:#555;margin-top:17px}
.card .more{display:flex;align-items:center;margin-top:24px;font-family:"Open Sans",sans-serif;font-size:11.5px;letter-spacing:.5px;color:#333}
.card .more::before{content:"";width:29px;height:1px;background:#b9b9b9;margin-right:13px}
.sale{position:absolute;left:116px;top:1442px;width:966px;height:465px;background:radial-gradient(ellipse at 50% 50%,#444 0%,#363636 50%,#252525 100%)}
.sale-text{position:absolute;left:116px;width:966px;text-align:center;color:#fff}
.btn{position:absolute;display:flex;align-items:center;justify-content:center;font-family:"Lora",serif;font-size:10.5px;font-weight:700;letter-spacing:.4px;text-transform:uppercase}
.product{position:absolute;top:2171px;text-align:center}
.product .photo{height:451px}
.product .name{font-family:"Lora",serif;font-size:15px;color:#333;margin-top:21px}
.product .price{font-family:"Roboto",sans-serif;font-weight:500;font-size:15px;color:var(--accent);margin-top:10px}
.join{position:absolute;left:0;top:2844px;width:1200px;height:223px;background:var(--band);text-align:center}
.join h3{position:absolute;top:45px;width:100%;font-family:"Roboto",sans-serif;font-weight:500;font-size:25px;color:#333}
.join p{position:absolute;top:97px;width:100%;font-family:"Roboto",sans-serif;font-weight:300;font-size:12.5px;color:#444}
.join .field{position:absolute;left:439px;top:146px;width:308px;height:31px;background:#fff;text-align:left;padding:9px 22px;font-family:"Roboto",sans-serif;font-size:9px;color:#b0b0b0}
.footer{position:absolute;left:0;top:3067px;width:1200px;height:336px;background:var(--footer);color:var(--footer-text)}
.f-col{position:absolute;font-family:"Lora",serif;font-size:13px}
.f-col div{white-space:nowrap}
.f-links{font-size:11.5px;font-weight:500;letter-spacing:.3px}
.social{position:absolute;width:26px;height:26px;border:1px solid #d9d9d9;border-radius:50%}
.to-top{position:absolute;left:1142px;top:277px;width:40px;height:39px;background:#3a3a3a}
</style>
</head>
<body>

<div class="grid-line" style="left:241px"></div>
<div class="grid-line" style="left:720px"></div>

<header>
  <div class="brand" style="top:32px;font-size:27px">
    <span class="brand-dot"></span>Harrow Lane
  </div>
  <svg class="tools" style="left:976px" width="110" height="22" viewBox="0 0 110 22" fill="none" stroke="#333" stroke-width="1.3">
    <rect x="3" y="8" width="11" height="10"/><path d="M5.5 8V5.5a3 3 0 0 1 6 0V8"/>
    <text x="15" y="7" font-size="7" fill="#333" stroke="none" font-family="Roboto">0</text>
    <circle cx="50" cy="10" r="5"/><path d="M54 14l4 4"/>
    <path d="M85 7h20M85 13h20"/>
  </svg>
  <nav class="nav">
    <span class="active" style="left:251px">Home</span>
    <span style="left:383px">Antique &amp; Vintage</span>
    <span style="left:558px">Antique Jewellery</span>
    <span style="left:682px">Art</span>
    <span style="left:777px">Furnishing</span>
    <span style="left:878px">Others</span>
    <span style="left:962px">Sale</span>
  </nav>
</header>

<section>
  <div class="hero" role="img" aria-label="Row of old leather-bound books on a wooden shelf"></div>
  <svg class="arrow" style="left:56px;top:366px" width="18" height="32" viewBox="0 0 18 32" fill="none" stroke="#fff" stroke-width="1.5"><path d="M16 2L2 16l14 14"/></svg>
  <svg class="arrow" style="left:1128px;top:366px" width="18" height="32" viewBox="0 0 18 32" fill="none" stroke="#fff" stroke-width="1.5"><path d="M2 2l14 14L2 30"/></svg>
  <div class="hero-box">
    <h2><em>ANTIQUE</em> FRENCH CROWN</h2>
    <p>Lorem ipsum dolor sit amet, consectetur ense adipisicing elit, sed do eiusmod inas alis dene tempor ins aliqua ut enim...</p>
    <a>Know More..</a>
  </div>
</section>

<section>
  <div class="kicker" style="top:737px">Unique &amp; Memorable</div>
  <div class="title" style="top:768px">OUR COLLECTION</div>
  <div class="rule" style="left:312px;top:787px;width:87px"></div>
  <div class="rule" style="left:801px;top:787px;width:87px"></div>

  <article class="card" style="left:116px">
    <div class="photo" role="img" aria-label="Wood-panelled hall with a staircase and crystal chandelier" style="background:linear-gradient(180deg,#4a4a4a,#2e2e2e 70%,#3c3c3c)"></div>
    <div class="label"><i>Collection</i><b>Antique &amp; Vintage</b></div>
    <p>Lorem ipsum dolor sit amet eiusmod, consectetur adip isi cing elit, sed do.</p>
    <div class="more">View more</div>
  </article>
  <article class="card" style="left:365px">
    <div class="photo" role="img" aria-label="Wire sculpture on a pale background" style="background:linear-gradient(180deg,#d6d6d6,#c2c2c2 60%,#8e8e8e)"></div>
    <div class="label"><i>Collection</i><b>Art &amp; Decoration</b></div>
    <p>Lorem ipsum dolor sit amet eiusmod, consectetur adip isi cing elit, sed do.</p>
    <div class="more">View more</div>
  </article>
  <article class="card" style="left:613px">
    <div class="photo" role="img" aria-label="Framed textile above a cabinet with a potted plant" style="background:linear-gradient(180deg,#6a6a6a,#959595 40%,#3f3f3f 70%,#4a4a4a)"></div>
    <div class="label"><i>Collection</i><b>Furnishing</b></div>
    <p>Lorem ipsum dolor sit amet eiusmod, consectetur adip isi cing elit, sed do.</p>
    <div class="more">View more</div>
  </article>
  <article class="card" style="left:862px">
    <div class="photo" role="img" aria-label="Jewelled crown on a stand against patterned wallpaper" style="background:linear-gradient(180deg,#cdcdcd,#777 50%,#383838)"></div>
    <div class="label"><i>Collection</i><b>Jewellery</b></div>
    <p>Lorem ipsum dolor sit amet eiusmod, consectetur adip isi cing elit, sed do.</p>
    <div class="more">View more</div>
  </article>
</section>

<section>
  <div class="sale" role="img" aria-label="Shelves of fabric rolls and ribbons in a workroom"></div>
  <div class="sale-text" style="top:1581px;font-family:'Lora',serif;font-style:italic;font-size:21px;color:#cfcfcf">Harrow Lane</div>
  <div class="sale-text" style="top:1614px;font-family:'Roboto',sans-serif;font-weight:300;font-size:44px;letter-spacing:1px">COLLECTION SALE</div>
  <div class="sale-text" style="top:1671px;font-family:'Roboto',sans-serif;font-size:12.5px;line-height:21px">Lorem ipsum dolor sit amet, consectetur adipisicing elit, sed do eius<br>mod tempor incididunt ut labore et dolore magna aliqua.</div>
  <div class="btn" style="left:558px;top:1738px;width:109px;height:38px;border:1px solid rgba(255,255,255,.6);color:#fff">Shop Now</div>
</section>

<section>
  <div class="kicker" style="top:2040px">Our Latest Collection</div>
  <div class="title" style="top:2071px">NEW ARRIVALS</div>
  <div class="rule" style="left:330px;top:2089px;width:88px"></div>
  <div class="rule" style="left:782px;top:2089px;width:88px"></div>

  <svg class="arrow" style="left:51px;top:2385px" width="14" height="26" viewBox="0 0 14 26" fill="none" stroke="#444" stroke-width="1.4"><path d="M12 2L2 13l10 11"/></svg>
  <svg class="arrow" style="left:1122px;top:2385px" width="14" height="26" viewBox="0 0 14 26" fill="none" stroke="#444" stroke-width="1.4"><path d="M2 2l10 11L2 24"/></svg>

  <div class="product" style="left:108px;width:312px">
    <div class="photo" role="img" aria-label="Fur hat with crown trim on a stack of books" style="background:linear-gradient(180deg,#dedede,#b8b8b8 35%,#3e3e3e 60%,#2c2c2c)"></div>
    <div class="name">Antique Item</div><div class="price">$800.00</div>
  </div>
  <div class="product" style="left:441px;width:311px">
    <div class="photo" role="img" aria-label="Star crown resting on old books" style="background:linear-gradient(180deg,#dcdcdc,#a6a6a6 40%,#4c4c4c 75%,#3c3c3c)"></div>
    <div class="name">Antique Item</div><div class="price">$1085.00</div>
  </div>
  <div class="product" style="left:778px;width:303px">
    <div class="photo" role="img" aria-label="Classical column and cornice with a small window" style="background:linear-gradient(180deg,#e2e2e2,#d4d4d4 60%,#bdbdbd)"></div>
    <div class="name">Antique Item</div><div class="price">$568.00</div>
  </div>

  <div class="btn" style="left:545px;top:2730px;width:109px;height:40px;border:1px solid var(--accent);color:#333">View More</div>
</section>

<section class="join">
  <h3>JOIN EMAIL</h3>
  <p>Sign up to receive the latest news and updates</p>
  <div class="field">Your email address</div>
  <svg class="abs" style="left:717px;top:154px" width="10" height="16" viewBox="0 0 10 16" fill="none" stroke="#333" stroke-width="1.6"><path d="M2 2l6 6-6 6"/></svg>
</section>

<footer class="footer">
  <div class="brand" style="top:54px;font-size:27px">
    <span class="brand-dot"></span>Harrow Lane
  </div>
  <div class="f-col" style="left:118px;top:156px;line-height:32px">
    <div>418 Wren Court Ashbury</div>
    <div>555-014-2718, 555-019-3364</div>
    <div>hello@harrowlane.example</div>
    <div>Copyright © Lantern Works 2019</div>
  </div>
  <div class="f-col f-links" style="left:435px;top:157px;line-height:26.5px">
    <div>Antique &amp; Vintage</div><div>Jewellery</div><div>Art</div><div>Furnishing</div><div>Others</div>
  </div>
  <div class="f-col f-links" style="left:637px;top:157px;line-height:26.5px">
    <div>Terms &amp; Conditions</div><div>Privacy Policy</div><div>Refund Policy</div><div>My Account</div>
  </div>
  <div class="f-col f-links" style="left:867px;top:157px;font-size:13px">Follow Us At:</div>
  <span class="social" style="left:866px;top:187px"></span>
  <span class="social" style="left:901px;top:187px"></span>
  <span class="social" style="left:936px;top:187px"></span>
  <span class="social" style="left:972px;top:187px"></span>
  <span class="social" style="left:1006px;top:187px"></span>
  <div class="to-top">
    <svg class="abs" style="left:13px;top:15px" width="14" height="9" viewBox="0 0 14 9" fill="none" stroke="#bbb" stroke-width="1.3"><path d="M1 8l6-6 6 6"/></svg>
  </div>
</footer>

</body>
</html>
```